Financial firm simple design

Classic business card design for a financial fund. 2 sided card- white on both sides.. One with just the company name centered and the other w the info. info included on that is :

Name
Company position
phone number
fax
email
website

Financial

```html
<!DOCTYPE html>
<html lang="en">
<head>
<meta charset="utf-8">
<title>Orvell Capital – Business Card</title>
<link rel="stylesheet" href="https://fonts.googleapis.com/css2?family=EB+Garamond:wght@400;500&display=swap">
<style>
  :root {
    --canvas-bg: #eceeef;
    --card-bg: #fbfbfa;
    --ink: #1b1d22;
    --ink-soft: #3a3d44;
    --frame: #23262c;
    --shadow: rgba(20, 24, 30, 0.14);
  }

  * { box-sizing: border-box; margin: 0; padding: 0; }

  html, body {
    width: 1200px;
    height: 860px;
    overflow: hidden;
  }

  body {
    background: var(--canvas-bg);
    font-family: "EB Garamond", Georgia, serif;
    color: var(--ink);
  }

  .card-set {
    position: absolute;
    inset: 0;
    display: flex;
    align-items: center;
    justify-content: center;
    gap: 44px;
  }

  .card {
    position: relative;
    width: 532px;
    height: 304px;
    background: var(--card-bg);
    box-shadow: 0 10px 28px var(--shadow), 0 1px 3px var(--shadow);
  }

  .card__frame {
    position: absolute;
    inset: 16px;
    border: 1.2px solid var(--frame);
  }

  /* Information side */
  .card--info .card__content {
    position: absolute;
    left: 44px;
    top: 40px;
  }

  .holder-name {
    font-size: 34px;
    font-weight: 500;
    letter-spacing: 0.2px;
    line-height: 1.1;
  }

  .holder-title {
    margin-top: 4px;
    font-size: 13.5px;
    color: var(--ink-soft);
  }

  .divider {
    width: 150px;
    height: 0;
    border-top: 1.2px solid var(--frame);
    margin: 12px 0 12px;
  }

  .contact-list {
    list-style: none;
    font-size: 14px;
    line-height: 1.85;
    color: var(--ink);
  }

  .contact-list .label {
    display: inline-block;
    width: 34px;
  }

  /* Name side */
  .card--brand {
    display: flex;
    align-items: center;
    justify-content: center;
  }

  .brand-name {
    position: relative;
    font-size: 31px;
    font-weight: 400;
    letter-spacing: 4px;
    text-transform: uppercase;
    color: var(--ink);
  }
</style>
</head>
<body>
  <main class="card-set">
    <section class="card card--info" aria-label="Contact side of business card">
      <div class="card__frame"></div>
      <div class="card__content">
        <h1 class="holder-name">Example Name</h1>
        <p class="holder-title">CEO - Orvell Capital</p>
        <div class="divider"></div>
        <ul class="contact-list">
          <li><span class="label">(T):</span>(555) 014-2387</li>
          <li><span class="label">(F):</span>(555) 014-2390</li>
          <li><span class="label">(E):</span>john@orvellcapital.com</li>
          <li><span class="label">(W):</span>www.orvellcapital.com</li>
        </ul>
      </div>
    </section>

    <section class="card card--brand" aria-label="Company side of business card">
      <div class="card__frame"></div>
      <p class="brand-name">Orvell Capital</p>
    </section>
  </main>
</body>
</html>
```